Simple and Clean business card design

We would like the design to be simple clean and to incorporate our colors.

We are open to your design and talent, we have the dots in our logo as we think of it as data points and we connect data points for people.

We are open to see the great creative and clean design you bring to the table

Contact Information for Business Card

please include: name, position, email, phone and website

Font styles to use
Sans Serif

Requirements
Must have
• my colors incorporated, simplicity
Nice to have
• lots of white space, simplicity
Should not have
• complexicity/ complex art

```html
<!DOCTYPE html>
<html lang="en">
<head>
<meta charset="UTF-8">
<title>Sporely Business Card</title>
<link href="https://fonts.googleapis.com/css2?family=Montserrat:wght@400;500;600;700&display=swap" rel="stylesheet">
<style>
  :root {
    --stage: #d4d4d4;
    --card-white: #ffffff;
    --card-black: #0b0b0d;
    --ink: #111111;
    --wordmark-dark: #5a5a5e;
    --blue: #4a78c2;
    --green: #2fa84a;
    --yellow: #f1b70f;
    --red: #e03a2e;
  }
  * { box-sizing: border-box; margin: 0; padding: 0; }
  html, body {
    width: 1200px; height: 900px; overflow: hidden;
    background: var(--stage);
    font-family: "Montserrat", sans-serif;
  }
  .stage {
    width: 1200px; height: 900px;
    display: flex; flex-direction: column;
    align-items: center; justify-content: center; gap: 36px;
  }
  .card {
    width: 700px; height: 400px;
    box-shadow: 0 10px 28px rgba(0,0,0,0.22);
    position: relative;
  }
  .card--back {
    background: var(--card-black);
    display: flex; align-items: center; justify-content: center;
  }
  .card--front {
    background: var(--card-white);
    display: flex; align-items: center;
  }
  .wordmark {
    display: flex; align-items: center; gap: 12px;
    font-weight: 600; letter-spacing: 0.5px; line-height: 1;
  }
  .wordmark__dot { width: 16px; height: 16px; border-radius: 50%; background: var(--blue); }
  .card--back .wordmark { font-size: 64px; color: var(--wordmark-dark); }
  .card--front .wordmark { font-size: 58px; color: var(--ink); }
  .card__brand {
    width: 330px; display: flex; justify-content: center;
    padding-left: 30px;
  }
  .card__divider {
    width: 2px; height: 150px; background: var(--yellow);
    margin: 0 36px 0 20px;
  }
  .contact__name {
    color: var(--blue); font-weight: 700; font-size: 27px;
    letter-spacing: 1px; line-height: 1.1;
  }
  .contact__role {
    font-size: 18px; font-weight: 500; color: var(--ink);
    margin-bottom: 22px;
  }
  .contact__list { list-style: none; }
  .contact__item {
    display: flex; align-items: center; gap: 10px;
    font-size: 18px; font-weight: 500; color: var(--ink);
    line-height: 1.45;
  }
  .contact__icon { width: 17px; height: 17px; flex: none; }
</style>
</head>
<body>
<main class="stage">
  <section class="card card--back" aria-label="Card back">
    <div class="wordmark">
      <span class="wordmark__dot"></span>
      <span class="wordmark__name">Sporely</span>
    </div>
  </section>

  <section class="card card--front" aria-label="Card front">
    <div class="card__brand">
      <div class="wordmark">
        <span class="wordmark__dot"></span>
        <span class="wordmark__name">Sporely</span>
      </div>
    </div>
    <div class="card__divider"></div>
    <div class="contact">
      <h1 class="contact__name">MARTIN COLE</h1>
      <p class="contact__role">Founder/ CEO</p>
      <ul class="contact__list">
        <li class="contact__item">
          <svg class="contact__icon" viewBox="0 0 24 24"><path fill="#e03a2e" d="M6.6 10.8a15.1 15.1 0 0 0 6.6 6.6l2.2-2.2c.3-.3.7-.4 1-.2 1.1.4 2.3.6 3.6.6.6 0 1 .4 1 1V20c0 .6-.4 1-1 1C10.6 21 3 13.4 3 4c0-.6.4-1 1-1h3.5c.6 0 1 .4 1 1 0 1.3.2 2.5.6 3.6.1.3 0 .7-.2 1z"/></svg>
          <span>555-210-3187</span>
        </li>
        <li class="contact__item">
          <svg class="contact__icon" viewBox="0 0 24 24"><rect x="2" y="5" width="20" height="14" fill="none" stroke="#2fa84a" stroke-width="2"/><path d="M2 5l10 8 10-8M2 19l7-7M22 19l-7-7" fill="none" stroke="#2fa84a" stroke-width="2"/></svg>
          <span>martin.cole@sporely.one</span>
        </li>
        <li class="contact__item">
          <svg class="contact__icon" viewBox="0 0 24 24" fill="none" stroke="#4a78c2" stroke-width="1.8"><circle cx="12" cy="12" r="9.5"/><ellipse cx="12" cy="12" rx="4.2" ry="9.5"/><path d="M2.5 12h19M4 7h16M4 17h16"/></svg>
          <span>www.Sporely.one</span>
        </li>
      </ul>
    </div>
  </section>
</main>
</body>
</html>
```